Criação de Papelaria para Arquitetura
A empresa queria:
" Escritório fundado por dois sócios ( Bordalo & Quintela ) com atuação desde a criação do projeto arquitetônico, compatibilização de projetos complementares e a construção - gerenciamento de obras. Maiores informações: www.bqarquitetos-exemplo.com.br "

```html
<!DOCTYPE html>
<html lang="pt-BR">
<head>
<meta charset="utf-8">
<title>Bordalo &amp; Quintela — Pasta institucional</title>
<link href="https://fonts.googleapis.com/css2?family=Montserrat:wght@400;600;800&display=swap" rel="stylesheet">
<style>
  :root {
    --backdrop: #e4e4e4;
    --paper: #ffffff;
    --paper-shade: #f3f3f3;
    --ink: #2a2a2a;
    --pocket: #111111;
    --pocket-mark: #4b4b4b;
    --photo-light: #d9d6d2;
    --photo-mid: #9a948e;
    --photo-dark: #5a5652;
  }
  * { margin: 0; padding: 0; box-sizing: border-box; }
  html, body { width: 1200px; height: 1200px; overflow: hidden; }
  body {
    background: var(--backdrop);
    font-family: "Montserrat", sans-serif;
    color: var(--ink);
  }
  .folder-spread {
    position: absolute;
    left: 80px; top: 240px;
    width: 1040px; height: 720px;
    display: flex;
    box-shadow: 0 18px 40px rgba(0,0,0,0.18);
  }
  .panel {
    position: relative;
    width: 520px; height: 720px;
    background: var(--paper);
    overflow: hidden;
  }
  .panel--left { background: linear-gradient(90deg, var(--paper) 85%, var(--paper-shade)); }
  .panel svg.photo-grid { position: absolute; left: 0; top: 0; }
  .history {
    position: absolute;
    left: 90px; top: 300px;
    width: 300px;
  }
  .history__title {
    font-weight: 800;
    font-size: 17px;
    letter-spacing: 1px;
    text-align: center;
    margin-bottom: 22px;
  }
  .history__text {
    font-size: 10.5px;
    line-height: 1.55;
    text-align: justify;
    margin-bottom: 10px;
  }
  .pocket { position: absolute; left: 0; top: 0; }
  .pocket__name {
    font-family: "Montserrat", sans-serif;
    font-weight: 800;
    font-size: 42px;
    fill: var(--pocket-mark);
  }
</style>
</head>
<body>
  <main class="folder-spread">
    <section class="panel panel--left">
      <svg class="photo-grid" width="520" height="720" viewBox="0 0 520 720">
        <defs>
          <linearGradient id="photoTone" x1="0" y1="0" x2="1" y2="1">
            <stop offset="0" stop-color="var(--photo-light)"/>
            <stop offset="1" stop-color="var(--photo-mid)"/>
          </linearGradient>
          <linearGradient id="photoDeep" x1="0" y1="0" x2="1" y2="1">
            <stop offset="0" stop-color="var(--photo-mid)"/>
            <stop offset="1" stop-color="var(--photo-dark)"/>
          </linearGradient>
        </defs>
        <g stroke="#ffffff" stroke-width="6">
          <polygon role="img" aria-label="Foto da fachada do escritório" points="180,0 240,60 180,120 120,60" fill="url(#photoDeep)"/>
          <polygon role="img" aria-label="Foto de interior comercial" points="300,0 360,60 300,120 240,60" fill="url(#photoTone)"/>
          <polygon role="img" aria-label="Foto de loja projetada" points="240,60 300,120 240,180 180,120" fill="url(#photoTone)"/>
          <polygon role="img" aria-label="Foto de ambiente de trabalho" points="360,60 420,120 360,180 300,120" fill="url(#photoDeep)"/>
          <polygon role="img" aria-label="Foto de sala de reuniões" points="300,120 360,180 300,240 240,180" fill="url(#photoTone)"/>
        </g>
      </svg>
      <article class="history">
        <h2 class="history__title">HISTÓRIA</h2>
        <p class="history__text">O escritório Bordalo &amp; Quintela nasceu da parceria entre dois arquitetos que compartilham a mesma paixão pelo projeto bem resolvido e pela obra bem executada.</p>
        <p class="history__text">Desde a concepção arquitetônica até a compatibilização dos projetos complementares, a equipe acompanha cada etapa com rigor técnico e atenção ao detalhe.</p>
        <p class="history__text">Na construção, o gerenciamento de obras garante prazos, custos e qualidade sob controle, com diálogo constante entre cliente, fornecedores e equipe.</p>
        <p class="history__text">Hoje, o escritório reúne projetos comerciais e residenciais em diversas cidades do país.</p>
      </article>
    </section>

    <section class="panel panel--right">
      <svg class="photo-grid" width="520" height="720" viewBox="0 0 520 720">
        <g stroke="#ffffff" stroke-width="6">
          <polygon role="img" aria-label="Foto de corredor de shopping" points="120,40 180,100 120,160 60,100" fill="url(#photoTone)"/>
          <polygon role="img" aria-label="Foto de vitrine de loja" points="240,40 300,100 240,160 180,100" fill="url(#photoDeep)"/>
          <polygon role="img" aria-label="Foto de teto e iluminação de loja" points="360,40 420,100 360,160 300,100" fill="url(#photoTone)"/>
          <polygon role="img" aria-label="Foto de fachada comercial" points="480,40 540,100 480,160 420,100" fill="url(#photoDeep)"/>
          <polygon role="img" aria-label="Foto de interior de loja de roupas" points="180,100 240,160 180,220 120,160" fill="url(#photoDeep)"/>
          <polygon role="img" aria-label="Foto de loja com letreiro vermelho" points="300,100 360,160 300,220 240,160" fill="url(#photoTone)"/>
          <polygon role="img" aria-label="Foto de loja de joias" points="420,100 480,160 420,220 360,160" fill="url(#photoTone)"/>
          <polygon role="img" aria-label="Foto de balcão de atendimento" points="360,160 420,220 360,280 300,220" fill="url(#photoDeep)"/>
        </g>
      </svg>
      <svg class="pocket" width="520" height="720" viewBox="0 0 520 720">
        <path d="M0,720 L0,470 Q0,420 60,420 L520,420 L520,720 Z" fill="var(--pocket)"/>
        <text class="pocket__name" x="260" y="520" text-anchor="middle">Bordalo &amp; Quintela</text>
      </svg>
    </section>
  </main>
</body>
</html>
```